Business Card Design for Photographer

Updating business card design. Must use included logo. We're a luxury wedding photography business. Elegancy, luxury, consistency are messages we wish to convey.

Visit our website at www.colvanderose.com to familiarize yourself more with our brand design currently (fonts, colors etc.). This is what we want to maintain.

Target Market(s)

Luxury Brides and Grooms

Industry/Entity Type

Wedding

Contact Information for Business Card

Current logo (attached to brief)
Name: Colin Vanderose
Phone: 5871302948
website/blog
Email

Requirements
Must have
• Current logo (attached to brief)
• Name: Colin Vanderose
• Phone: 5871302948
• website/blog
• Email
• Instagram username
Should not have
• bright colors, fonts that don't suit our brand (visit www.colvanderose.com)

```html
<!DOCTYPE html>
<html lang="en">
<head>
<meta charset="utf-8">
<title>Colin Vanderose Photographers – Business Cards</title>
<link href="https://fonts.googleapis.com/css2?family=Tenor+Sans&family=Roboto:wght@400;500&display=swap" rel="stylesheet">
<style>
  :root {
    --backdrop: #2a2a2a;
    --card-white: #ffffff;
    --card-mist: #e9e9e9;
    --card-grey: #6b6b6b;
    --ink-grey: #6a6a6a;
    --ink-soft: #7a7a7a;
    --band-grey: #8c8c8c;
    --rule-grey: #b5b5b5;
    --ink-light: #ffffff;
  }
  * { margin: 0; padding: 0; box-sizing: border-box; }
  html, body {
    width: 1200px; height: 848px; overflow: hidden;
    background: var(--backdrop);
  }
  .canvas { position: relative; width: 1200px; height: 848px; }

  .card { position: absolute; box-shadow: 0 6px 18px rgba(0,0,0,.45); overflow: hidden; }

  /* Front (vertical) */
  .card-front {
    left: 234px; top: 132px; width: 216px; height: 564px;
    background: radial-gradient(ellipse 70% 40% at 50% 32%, var(--card-white) 40%, var(--card-mist) 100%);
  }
  .card-front .bottom-band { position: absolute; left: 0; bottom: 0; width: 216px; height: 40px; }

  .brand { position: absolute; left: 0; width: 100%; text-align: center; font-family: "Tenor Sans", sans-serif; font-weight: 400; }
  .brand-mark { display: block; margin: 0 auto; }
  .brand-name { text-transform: uppercase; white-space: nowrap; }
  .brand-tag { text-transform: uppercase; white-space: nowrap; }

  .card-front .brand { top: 150px; color: var(--ink-grey); }
  .card-front .brand-mark { width: 40px; height: 40px; background: var(--ink-grey); }
  .card-front .brand-name { margin-top: 10px; font-size: 16px; letter-spacing: 1.8px; }
  .card-front .brand-tag { margin-top: 6px; font-size: 10px; letter-spacing: 3.2px; }

  .contact { position: absolute; left: 0; top: 386px; width: 100%; text-align: center; font-family: "Roboto", sans-serif; color: var(--ink-soft); }
  .contact-name { font-size: 15px; font-weight: 500; color: var(--ink-grey); }
  .contact-rule { width: 180px; height: 1px; margin: 8px auto 10px; background: linear-gradient(90deg, transparent, var(--rule-grey) 20%, var(--rule-grey) 80%, transparent); }
  .contact-list { list-style: none; font-size: 11.5px; line-height: 20px; }
  .contact-list li { display: flex; justify-content: center; align-items: center; gap: 4px; }
  .contact-list svg { width: 10px; height: 10px; fill: var(--ink-soft); flex: none; }

  /* Back (horizontal) */
  .card-back { left: 524px; top: 246px; width: 540px; height: 310px; background: var(--card-grey); }
  .card-back .brand { top: 90px; color: var(--ink-light); }
  .card-back .brand-mark { width: 54px; height: 54px; background: var(--ink-light); }
  .card-back .brand-name { margin-top: 14px; font-size: 25px; letter-spacing: 3px; }
  .card-back .brand-tag { margin-top: 8px; font-size: 13px; letter-spacing: 4.5px; }
</style>
</head>
<body>
<main class="canvas">

  <section class="card card-front" aria-label="Business card front">
    <div class="brand">
      <span class="brand-mark" aria-hidden="true"></span>
      <p class="brand-name">Colin Vanderose</p>
      <p class="brand-tag">Photographers</p>
    </div>

    <div class="contact">
      <p class="contact-name">Colin Vanderose</p>
      <div class="contact-rule"></div>
      <ul class="contact-list">
        <li>
          <svg viewBox="0 0 10 10" aria-hidden="true"><path d="M1 3.5C1 2 2 1.5 5 1.5S9 2 9 3.5L7 4V3H3v1zM2.5 5h5l1 3.5h-7z"/></svg>
          (587) 130-2948
        </li>
        <li>
          <svg viewBox="0 0 10 10" aria-hidden="true"><rect x="0.5" y="2" width="9" height="6.5" rx="1"/></svg>
          colin@colvanderose.com
        </li>
        <li>
          <svg viewBox="0 0 10 10" aria-hidden="true"><path d="M5 .5a4.5 4.5 0 1 0 0 9 4.5 4.5 0 0 0 0-9zm0 1c.6.6 1.1 1.7 1.2 3H3.8C3.9 3.2 4.4 2.1 5 1.5zM1.5 5.5h1.3c.1 1 .4 1.9.8 2.6A3.5 3.5 0 0 1 1.5 5.5zm0-1a3.5 3.5 0 0 1 2.1-2.6c-.4.7-.7 1.6-.8 2.6zm3.5 4c-.6-.6-1.1-1.7-1.2-3h2.4c-.1 1.3-.6 2.4-1.2 3zm1.4-.4c.4-.7.7-1.6.8-2.6h1.3a3.5 3.5 0 0 1-2.1 2.6zm.8-3.6c-.1-1-.4-1.9-.8-2.6a3.5 3.5 0 0 1 2.1 2.6z"/></svg>
          colvanderose.com
        </li>
        <li>
          <svg viewBox="0 0 10 10" aria-hidden="true"><rect x="1" y="1" width="8" height="8"/></svg>
          colvanderosephoto
        </li>
      </ul>
    </div>

    <svg class="bottom-band" viewBox="0 0 216 40" preserveAspectRatio="none" aria-hidden="true">
      <path d="M0 14 Q108 -6 216 14 V40 H0 Z" fill="var(--band-grey)"/>
    </svg>
  </section>

  <section class="card card-back" aria-label="Business card back">
    <div class="brand">
      <span class="brand-mark" aria-hidden="true"></span>
      <p class="brand-name">Colin Vanderose</p>
      <p class="brand-tag">Photographers</p>
    </div>
  </section>

</main>
</body>
</html>
```